Time for a better IT consulting company?

We are a mobile computer consulting company, taking care of client's issues remotely or at their site. Website of company www.harbor-techmend.com. Business card is an example of marketing so far.
We moved this year but we still service our existing clients. We have expanded our number of technicians available. We would like to use this card for both new business and reaching out to old business.

Target Market(s)

This should target businesses and referrals to businesses from our existing clients as well as a new client outreach for our new location.

Industry/Entity Type

Computer

Requirements
Must have
• This postcard will let clients know we have moved into or we continue to service their area. Make sure it says Inc, not LLC. Must incorporate existing theme in some fashion.
Nice to have
• Themes to communicate: team of people standing by, stability, faster response time, accessibility.
• Areas of coverage: Westchester, Rockland, Manhattan, The Bronx, lower Connecticut.
Should not have
• Cartoon feel.

```html
<!DOCTYPE html>
<html lang="en">
<head>
<meta charset="utf-8">
<title>Harbor Techmend Computer Consulting – Postcard</title>
<link rel="stylesheet" href="https://fonts.googleapis.com/css2?family=Arimo:wght@400;700&family=Roboto+Condensed:wght@700&display=swap">
<style>
  :root {
    --sky: #1ba7e5;
    --ink: #1f1f1f;
    --ink-soft: #3b3b3b;
    --slate: #5d5f62;
    --white: #ffffff;
    --accent: #f3e600;
    --rule: #8a8a8a;
  }
  * { margin: 0; padding: 0; box-sizing: border-box; }
  html, body { width: 1200px; height: 924px; overflow: hidden; background: var(--white); }
  .postcard {
    position: relative;
    width: 1200px;
    height: 924px;
    background: var(--white);
    font-family: "Arimo", Arial, sans-serif;
    color: var(--ink);
    overflow: hidden;
  }
  .hero-panel {
    position: absolute; left: 545px; top: 0;
    width: 655px; height: 425px;
    background: var(--sky);
  }
  .team-photo {
    position: absolute; left: 0; top: 0;
    width: 545px; height: 425px;
    background: linear-gradient(135deg, #e9edf1 0%, #c9d0d8 45%, #7b848e 80%, #d7dde3 100%);
  }
  .headline {
    position: absolute; left: 593px; top: 45px;
    color: var(--white);
    font-size: 52px; line-height: 60px;
    text-transform: uppercase;
    letter-spacing: 0.3px;
  }
  .headline strong { font-weight: 700; }
  .headline span { font-weight: 400; }
  .feature-circle {
    position: absolute; top: 255px;
    width: 260px; height: 260px;
    border-radius: 50%;
    background: var(--white);
    border: 4px solid var(--sky);
    padding: 8px;
  }
  .feature-circle .photo { width: 100%; height: 100%; border-radius: 50%; }
  .circle-servers { left: 338px; }
  .circle-servers .photo { background: linear-gradient(160deg, #dfe6ec 0%, #a9b4bf 50%, #3d4753 100%); }
  .circle-meeting { left: 615px; }
  .circle-meeting .photo { background: linear-gradient(160deg, #f4f4f2 0%, #d9d3cc 55%, #8d8f94 100%); }
  .circle-tech { left: 905px; }
  .circle-tech .photo { background: radial-gradient(circle at 60% 45%, #4a9fd0 0%, #1f5f8e 45%, #0b2238 100%); }
  .intro {
    position: absolute; left: 60px; top: 542px;
    width: 1070px;
    font-size: 24.5px; line-height: 30px;
    color: var(--ink);
  }
  .brand {
    position: absolute; left: 85px; top: 700px;
    display: flex; align-items: center; gap: 16px;
    color: var(--ink-soft); font-weight: 700;
  }
  .brand-mark { width: 106px; height: 106px; border-radius: 50%; background: var(--sky); flex: none; }
  .brand-name { font-size: 30px; line-height: 34px; letter-spacing: 1px; }
  .brand-sub { font-size: 13px; letter-spacing: 4.5px; margin-top: 6px; }
  .divider {
    position: absolute; left: 580px; top: 705px;
    width: 1px; height: 115px; background: var(--rule);
  }
  .contact-title {
    position: absolute; left: 641px; top: 728px;
    font-size: 33px; font-weight: 700; color: var(--sky);
  }
  .contact-line {
    position: absolute; left: 606px; top: 781px;
    display: flex; align-items: center;
    font-weight: 700; color: var(--ink-soft);
  }
  .contact-line svg { width: 28px; height: 28px; margin-right: 4px; }
  .contact-line .phone { font-size: 26px; }
  .contact-line .web { font-size: 22px; margin-left: 28px; }
  .coverage {
    position: absolute; left: 0; top: 840px;
    width: 1200px; height: 58px;
    display: flex;
    font-family: "Roboto Condensed", "Arial Narrow", sans-serif;
    font-weight: 700; font-size: 27px; color: var(--white);
    text-transform: uppercase;
  }
  .coverage-label {
    width: 183px; background: var(--slate);
    display: flex; align-items: center; justify-content: center;
  }
  .coverage-list {
    flex: 1; background: var(--sky);
    display: flex; align-items: center; padding-left: 20px;
    list-style: none;
  }
  .coverage-list li { display: flex; align-items: center; }
  .coverage-list li + li::before {
    content: ""; display: inline-block;
    width: 4px; height: 30px; background: var(--accent);
    margin: 0 16px;
  }
</style>
</head>
<body>
<main class="postcard">
  <div class="hero-panel"></div>
  <div class="team-photo" role="img" aria-label="Photo of a smiling team of four consultants giving thumbs up"></div>

  <h1 class="headline"><strong>Need immediate<br>assistance</strong> <span>with a<br>computer issue?</span></h1>

  <div class="feature-circle circle-servers"><div class="photo" role="img" aria-label="Photo of two technicians with a laptop in a server room"></div></div>
  <div class="feature-circle circle-meeting"><div class="photo" role="img" aria-label="Photo of a team meeting around a table"></div></div>
  <div class="feature-circle circle-tech"><div class="photo" role="img" aria-label="Photo of a technician lit by blue screen light"></div></div>

  <p class="intro">For 18 years, my company has provided computer support to residents and businesses. This year we moved to Westchester County, and we still proudly serve all of our existing clients. We have also expanded our team, so more technicians are standing by to reach you faster, on site or remotely.</p>

  <div class="brand">
    <div class="brand-mark"></div>
    <div>
      <div class="brand-name">HARBOR TECHMEND</div>
      <div class="brand-sub">COMPUTER CONSULTING, INC</div>
    </div>
  </div>

  <div class="divider"></div>

  <h2 class="contact-title">GET CONNECT WITH US:</h2>
  <div class="contact-line">
    <svg viewBox="0 0 28 28" aria-hidden="true">
      <circle cx="14" cy="14" r="12" fill="none" stroke="#1ba7e5" stroke-width="2.4"/>
      <path d="M10 8.5c-1.2.8-1.5 2.6-.7 4.6 1 2.5 3 4.8 5.3 6 1.8.9 3.4.7 4.3-.4l-2.2-2.2-1.8.9c-1.3-.7-2.5-2-3.2-3.3l.9-1.8L10 8.5z" fill="#1ba7e5"/>
    </svg>
    <span class="phone">914-555-0172</span>
    <span class="web">www.harbor-techmend.com</span>
  </div>

  <div class="coverage">
    <div class="coverage-label">Serving</div>
    <ul class="coverage-list">
      <li>Westchester</li>
      <li>Rockland</li>
      <li>Manhattan</li>
      <li>The Bronx</li>
      <li>Lower Connecticut</li>
    </ul>
  </div>
</main>
</body>
</html>
```